Need Catering Menu designed - design that we want is attached

Hi,
We need a new catering menu designed for our cafe.
I have attached our coffee menu, we would like it to follow the same kind of layout.
It needs to be A4, and can be double sided.
I have attached a word doc of our catering menu, so this is what needs to be on the catering menu you produce.
Also, our contact details need to be on both sides of the menu:
Visit us instore to discuss catering options, or call 0438 672 914 or email martha@velbrisco.com.au
I have also attached our new logo which I'd like incorporated into the menu
Doctors/Nurses
Hospital staff
University Students
Catering

```html
<!DOCTYPE html>
<html lang="en">
<head>
<meta charset="utf-8">
<title>Ward Nine – Catering Menu</title>
<link rel="stylesheet" href="https://fonts.googleapis.com/css2?family=Arvo:wght@400;700&family=Oswald:wght@400;500&family=Open+Sans:wght@400&family=PT+Serif:wght@400&family=Special+Elite&display=swap">
<style>
:root{
  --board:#1b1b1b;
  --board-light:#2a2a2a;
  --chalk:#ffffff;
  --chalk-soft:#d8d8d8;
  --chalk-dim:#9a9a9a;
  --lemon:#f4ee8c;
  --brand-dark:#3a2c2c;
}
*{margin:0;padding:0;box-sizing:border-box}
html,body{width:848px;height:1200px;overflow:hidden;background:var(--board)}
.menu{
  position:relative;width:848px;height:1200px;overflow:hidden;
  background:radial-gradient(ellipse at 50% 30%,var(--board-light) 0%,var(--board) 70%);
  color:var(--chalk);font-family:"Arvo",serif;
}
.abs{position:absolute}
.brand{left:355px;top:40px;width:122px;height:109px;background:var(--lemon);
  display:flex;align-items:center;justify-content:center;
  font-family:"Arvo",serif;font-weight:700;font-size:17px;color:var(--brand-dark);letter-spacing:1px}
.tagline{left:0;width:848px;top:160px;text-align:center;font-family:"Special Elite",monospace;color:var(--lemon);font-size:17px}
.frame{border:1.5px solid var(--chalk-soft)}
.banner{display:flex;align-items:center;justify-content:center}
.banner svg{position:absolute;inset:0;width:100%;height:100%}
.banner span{position:relative;font-family:"Oswald",sans-serif;font-size:19px;letter-spacing:.5px;text-transform:uppercase;color:var(--chalk)}
.price-list{list-style:none;font-weight:700;font-size:12.5px;line-height:15.1px}
.price-list li{display:flex}
.price-list .item{flex:1}
.price-list .price{width:58px}
.note{font-family:"PT Serif",serif;color:var(--lemon);font-size:9.5px;line-height:17px;padding:0 0 0 40px;white-space:nowrap;
  display:flex;flex-direction:column;justify-content:center}
.contact{left:0;width:848px;text-align:center;font-family:"Open Sans",sans-serif;font-size:9.5px;color:var(--chalk)}
.divider{left:0;width:848px;top:602px;height:1px;background:var(--chalk-dim)}
.col{display:flex;flex-direction:column}
.group-head{display:flex;justify-content:space-between;font-weight:700;font-size:13px;color:var(--lemon)}
.group-head .price{color:var(--chalk)}
.group-sub{font-family:"Open Sans",sans-serif;font-size:8px;color:var(--chalk-dim);line-height:11px}
.group-sub.lemon{font-family:"PT Serif",serif;color:var(--lemon);font-size:9.5px}
.dish{margin-top:5px}
.dish h3{font-weight:700;font-size:12.5px;line-height:16px}
.dish p{font-family:"PT Serif",serif;font-size:11px;line-height:14px;color:var(--chalk-soft)}
.hot-list{list-style:none;font-weight:700;font-size:12.5px;line-height:20px}
.hot-list li{display:flex;justify-content:space-between}
</style>
</head>
<body>
<main class="menu">
  <div class="abs brand">WARD NINE</div>
  <p class="abs tagline">catering menu</p>

  <section class="abs frame" style="left:60px;top:227px;width:344px;height:242px;padding:33px 0 0 56px">
    <ul class="price-list">
      <li><span class="item">fruit Platter</span><span class="price">$15</span></li>
      <li><span class="item">bacon Egg and Cheese Roll</span><span class="price">$6.5</span></li>
      <li><span class="item">vegetarian Brekky Wrap</span><span class="price">$6.5</span></li>
      <li><span class="item">ham and Cheese Croissant</span><span class="price">$6</span></li>
      <li><span class="item">cheese and Tomato Croissant</span><span class="price">$5.5</span></li>
      <li><span class="item">ham and Cheese French Toas</span><span class="price">$6.5</span></li>
      <li><span class="item">assorted Yoghurts</span><span class="price">$5.5</span></li>
      <li><span class="item">bircher muesli</span><span class="price">$5.5</span></li>
      <li><span class="item">chia pudding</span><span class="price">$5.5</span></li>
      <li><span class="item">granola and yoghurt</span><span class="price">$5.5</span></li>
      <li><span class="item">muffin</span><span class="price">$4.5</span></li>
      <li><span class="item">mini Muffin</span><span class="price">$2.5</span></li>
      <li><span class="item">juice</span><span class="price">$8</span></li>
    </ul>
  </section>
  <div class="abs banner" style="left:133px;top:209px;width:180px;height:31px">
    <svg viewBox="0 0 180 31" preserveAspectRatio="none"><polygon points="1,1 179,1 168,15.5 179,30 1,30 12,15.5" fill="#1b1b1b" stroke="#fff" stroke-width="1.5"/></svg>
    <span>Breakfast</span>
  </div>

  <section class="abs frame" style="left:439px;top:227px;width:341px;height:169px;padding:29px 0 0 57px">
    <ul class="price-list">
      <li><span class="item">fruit platter</span><span class="price">$15</span></li>
      <li><span class="item">muffin</span><span class="price">$4.5</span></li>
      <li><span class="item">mini muffin</span><span class="price">$2.5</span></li>
      <li><span class="item">assorted slices</span><span class="price">$4</span></li>
      <li><span class="item">assorted cookies from</span><span class="price">$3</span></li>
      <li><span class="item">assorted yoghurts</span><span class="price">$5.5</span></li>
      <li><span class="item">chia pudding</span><span class="price">$5.5</span></li>
      <li><span class="item">banana bread</span><span class="price">$4.5</span></li>
      <li><span class="item">juice</span><span class="price">$8</span></li>
    </ul>
  </section>
  <div class="abs banner" style="left:496px;top:209px;width:224px;height:31px">
    <svg viewBox="0 0 224 31" preserveAspectRatio="none"><polygon points="1,1 223,1 212,15.5 223,30 1,30 12,15.5" fill="#1b1b1b" stroke="#fff" stroke-width="1.5"/></svg>
    <span>Morning &amp; Afternoon</span>
  </div>
  <section class="abs frame note" style="left:439px;top:422px;width:341px;height:47px">
    <span>Cups/Plates/Serviettes can be provided at a charge of $1 per person</span>
    <span>Barista made coffee available</span>
  </section>

  <p class="abs contact" style="top:574px">Visit us instore to discuss catering options, or call 0438 672 914 or email martha@velbrisco.com.au</p>
  <div class="abs divider"></div>

  <section class="abs frame" style="left:29px;top:629px;width:787px;height:415px"></section>
  <div class="abs banner" style="left:29px;top:613px;width:164px;height:30px">
    <svg viewBox="0 0 164 30" preserveAspectRatio="none"><polygon points="1,1 163,1 152,15 163,29 1,29 1,15" fill="#1b1b1b" stroke="#fff" stroke-width="1.5"/></svg>
    <span>Lunch</span>
  </div>

  <div class="abs col" style="left:55px;top:653px;width:212px">
    <div class="group-head"><span>Sandwiches &nbsp;or Wraps</span><span class="price">$7.50</span></div>
    <p class="group-sub">Sandwiches cut into quarters – Wraps cut into thirds</p>
    <div class="dish" style="margin-top:21px"><h3>Ham</h3><p>butter, pickle spread, cheese, tomato,<br>champgne leg ham</p></div>
    <div class="dish"><h3>Turkey</h3><p>butter, cranberry sauce, lettuce mix,<br>tomato, turkey breast</p></div>
    <div class="dish"><h3>Sweet Chilli Chicken</h3><p>butter, sweet chilli sauce, aioli, lettuce mix,<br>tomato, cheese, sweet chilli chicken tenders</p></div>
    <div class="dish"><h3>Chicken Schnitzel</h3><p>butter, aioli, lettuce mix, tomato, tasty cheese,<br>chicken schnitzel</p></div>
    <div class="dish"><h3>Chicken and Avocado</h3><p>butter, aioli, lettuce mix, tomato, cheese,<br>chicken breast, avocado</p></div>
    <div class="dish"><h3>Egg</h3><p>butter, lettuce mix, egg, aioli, parsley,<br>spring onion</p></div>
    <div class="dish" style="margin-top:10px"><h3>Felafel</h3></div>
  </div>

  <div class="abs col" style="left:296px;top:653px;width:232px">
    <div class="dish" style="margin-top:0"><h3>Tandoori Chicken</h3><p>butter, tzatziki, lettuce mix, tomato,<br>tandoori chicken</p></div>
    <div class="dish"><h3>Waldorf Chicken</h3><p>butter, cos lettuce, chicken, seeded mustard,<br>celery, walnuts, aioli</p></div>
    <div class="dish"><h3>Chicken Ceasar</h3><p>butter, aioli, cos lettuce, chicken, parmesan<br>cheese, bacon</p></div>
    <div class="dish"><h3>Cajun Chicken</h3><p>butter, lettuce mix, tomato, red onion,<br>Cajun chicken</p></div>
    <div class="dish"><h3>Barbeque Chicken</h3><p>butter, BBQ,<br>chicken</p></div>
    <div class="dish"><h3>B.L.T.</h3><p>butter, aioli, lettuce, tomato, bacon</p></div>
    <div class="dish"><h3>Salad</h3><p>butter, lettuce mix, red onion, cucumber,<br>capsicum, tomato, avocado, tasty cheese</p></div>
    <div class="dish"><h3>Tuna</h3><p>butter, lettuce, tuna, aioli, sundried tomato,<br>spring onion</p></div>
  </div>

  <div class="abs col" style="left:553px;top:653px;width:252px">
    <div class="group-head"><span>Foccacias</span><span class="price">$8.50</span></div>
    <p class="group-sub">Cut in half – please let us know if you want them toasted</p>
    <p class="group-sub lemon">Same options as wraps and sandwiches &nbsp;plus</p>
    <div class="dish" style="margin-top:11px"><h3>Roast Veggie</h3><p>butter, pesto, grilled eggplant, grilled zucchini,<br>roasted capsicum, feta cheese, baby spinach</p></div>
    <div class="dish"><h3>Salami</h3><p>butter, pesto, baby spinach, mild salami,<br>roasted capsicum, olives, feta cheese</p></div>
    <div class="dish"><h3>Chicken Schnitzel</h3><p>Butter, Housemade coleslaw, chicken schnitzel</p></div>
    <div class="group-head" style="margin-top:58px"><span>Bagels</span><span class="price">$9.0</span></div>
    <div class="dish" style="margin-top:14px"><h3>Turkey</h3><p>butter, cranberry sauce, baby spinach, tomato,<br>camembert cheese</p></div>
    <div class="dish"><h3>Smoked Salmon</h3><p>butter, cream cheese, baby spinach, tomato, smoked<br>salmon</p></div>
  </div>

  <section class="abs frame" style="left:29px;top:1060px;width:787px;height:113px"></section>
  <div class="abs banner" style="left:29px;top:1048px;width:164px;height:30px">
    <svg viewBox="0 0 164 30" preserveAspectRatio="none"><polygon points="1,1 163,1 152,15 163,29 1,29 12,15" fill="#1b1b1b" stroke="#fff" stroke-width="1.5"/></svg>
    <span>Hot Food</span>
  </div>
  <ul class="abs hot-list" style="left:53px;top:1086px;width:196px">
    <li><span>Assorted Pies</span><span>$5.0</span></li>
    <li><span>Large tray hot chips</span><span>$15</span></li>
    <li><span>Small tray hot chips</span><span>$9</span></li>
    <li><span>Mini samosa</span><span>$3</span></li>
  </ul>
  <ul class="abs hot-list" style="left:296px;top:1066px;width:204px">
    <li><span>Vegetarian spring rolls</span><span>$3</span></li>
    <li><span>Party pies</span><span>$3</span></li>
    <li><span>Mini sausage rolls</span><span>$3</span></li>
    <li><span>Mini quiche</span><span>$3</span></li>
    <li><span>Mini dim sim</span><span>$2</span></li>
  </ul>
  <ul class="abs hot-list" style="left:553px;top:1066px;width:238px">
    <li><span>Sweet chilli chicken tenders</span><span>$3</span></li>
    <li><span>Meatballs</span><span>$2</span></li>
    <li><span>Spinach and ricotta pastizi</span><span>$3</span></li>
    <li><span>Vegetarian Frittata</span><span>$4.5</span></li>
    <li><span>Meat Frittata</span><span>$4.5</span></li>
  </ul>

  <p class="abs contact" style="top:1177px">Visit us instore to discuss catering options, or call 0438 672 914 or email martha@velbrisco.com.au</p>
</main>
</body>
</html>
```